Medical group practice

We need a flyer design incorporating the three doctors in the practice, there is a general practitioner, ophthalmologist and an obstetrician & Gynaecologist. see the attached file for the concept. will leave the colour design up to you

Target Market(s)

general public

Industry/Entity Type

Health Care

Colors

Designer to choose colors to be used in the design.

Requirements
Must have
• logos included in attachement

```html
<!DOCTYPE html>
<html lang="en">
<head>
<meta charset="utf-8">
<title>Northvale Medical – Flyer</title>
<link href="https://fonts.googleapis.com/css2?family=Cinzel:wght@400;500&family=Lato:ital,wght@0,400;0,700;1,400;1,700&display=swap" rel="stylesheet">
<style>
  :root{
    --bg:#4b4851;
    --dark:#3a3a3c;
    --red:#e31d25;
    --light:#ececec;
    --white:#ffffff;
    --ink:#1d1d1d;
    --teal:#1b8fb0;
    --purple:#7a2a86;
    --navy:#1d3f8a;
  }
  *{margin:0;padding:0;box-sizing:border-box}
  html,body{width:1200px;height:1200px;overflow:hidden;background:var(--bg)}
  .flyer{position:absolute;left:196px;top:28px;width:808px;height:1143px;background:var(--dark);overflow:hidden;font-family:'Lato',sans-serif}
  .flyer-shapes{position:absolute;inset:0}
  .abs{position:absolute}
  .brand{left:70px;top:84px;display:flex;align-items:center;gap:16px}
  .brand-dot{width:34px;height:34px;border-radius:50%;background:var(--red)}
  .brand-name{font-family:'Cinzel',serif;font-weight:400;font-size:29px;line-height:33px;color:#555;letter-spacing:1px}
  .headline{left:442px;top:38px;font-family:'Cinzel',serif;font-weight:400;color:var(--white);line-height:50px}
  .headline .l1{font-size:50px;display:block}
  .headline .l2{font-size:40px;display:block}
  .contact{left:65px;top:548px;color:var(--white);font-style:italic;font-size:15px;line-height:18px}
  .service-icon{left:474px;top:542px;width:56px;height:56px;background:var(--teal);border-radius:6px}
  .eye-doc{left:460px;top:632px;font-style:italic;font-size:15px;line-height:18.5px;color:var(--ink)}
  .red{color:var(--red)}
  .eye-doc .name{font-size:17px}
  .vision-brand{left:68px;top:790px;display:flex;align-items:center;gap:8px;font-size:12px;font-weight:700;line-height:15px;color:var(--purple)}
  .vision-brand .dot{width:14px;height:14px;border-radius:50%;background:var(--purple);flex:none}
  .gp{left:239px;top:754px;font-style:italic;font-size:14.5px;line-height:18px;color:var(--ink)}
  .gp .name{font-size:16.5px}
  .gp-list{left:526px;top:752px;list-style:none;font-style:italic;font-size:14.5px;line-height:18px;color:var(--ink)}
  .gp-list li{position:relative;padding-left:22px}
  .gp-list li::before{content:"";position:absolute;left:0;top:5px;width:8px;height:8px;border-radius:50%;background:var(--red)}
  .obgyn-brand{left:175px;top:990px;display:flex;align-items:center;gap:8px;font-size:14px;font-weight:700;line-height:17px;color:var(--navy)}
  .obgyn-brand .dot{width:20px;height:20px;border-radius:50%;background:var(--navy);flex:none}
  .obgyn{left:328px;top:952px;font-style:italic;font-size:13.3px;line-height:16.5px;color:var(--ink);width:450px}
  .obgyn .name{font-size:16px}
</style>
</head>
<body>
<main class="flyer">
  <svg class="flyer-shapes" width="808" height="1143" viewBox="0 0 808 1143" aria-hidden="true">
    <defs>
      <linearGradient id="photoTone" x1="0" y1="0" x2="1" y2="1">
        <stop offset="0" stop-color="#dfe8ef"/>
        <stop offset=".5" stop-color="#f4f8fb"/>
        <stop offset="1" stop-color="#cfe0ee"/>
      </linearGradient>
      <linearGradient id="bandTone" x1="0" y1="0" x2="0" y2="1">
        <stop offset="0" stop-color="#fafafa"/>
        <stop offset="1" stop-color="#e2e2e2"/>
      </linearGradient>
    </defs>
    <path d="M395,0 L425,0 C390,140 300,250 20,280 L0,262 C260,240 360,130 395,0Z" fill="var(--red)"/>
    <path d="M0,0 L378,0 C350,140 260,235 0,245Z" fill="var(--light)"/>
    <path d="M440,200 C560,165 700,160 808,182 L808,208 C700,185 560,190 440,220Z" fill="var(--red)"/>
    <path d="M0,320 C30,400 70,450 120,475 C220,510 320,512 380,508 C372,600 350,680 330,727 L0,727Z" fill="var(--red)"/>
    <path d="M380,512 C500,503 600,505 680,522 C740,565 780,640 807,700 L807,727 L332,727 C360,640 378,570 380,512Z" fill="var(--light)"/>
    <rect x="0" y="727" width="808" height="6" fill="var(--dark)"/>
    <rect x="0" y="733" width="808" height="186" fill="url(#bandTone)"/>
    <rect x="0" y="919" width="808" height="6" fill="var(--dark)"/>
    <rect x="0" y="925" width="808" height="168" fill="url(#bandTone)"/>
    <path d="M0,925 L150,925 C120,1010 80,1100 30,1143 L0,1143Z" fill="var(--red)"/>
    <path d="M150,925 L165,925 C140,1010 110,1090 70,1143 L30,1143 C80,1100 120,1010 150,925Z" fill="var(--dark)"/>
    <rect x="0" y="1093" width="808" height="50" fill="var(--dark)"/>
    <path d="M0,1093 L60,1093 C50,1115 40,1130 30,1143 L0,1143Z" fill="var(--red)"/>
  </svg>

  <svg class="abs" style="left:0;top:0" width="808" height="520" viewBox="0 0 808 520" role="img" aria-label="Photo of a team of four smiling doctors in white coats">
    <path d="M45,282 C160,280 260,250 365,212 C430,188 470,176 515,172 C640,170 740,180 807,192 L807,477 C740,458 700,458 640,470 C540,500 420,510 300,505 C200,500 130,485 95,472 C40,420 15,370 5,322 C20,300 30,290 45,282Z" fill="url(#photoTone)"/>
  </svg>

  <div class="abs brand"><span class="brand-dot"></span><div class="brand-name">NORTHVALE<br>MEDICAL</div></div>

  <h1 class="abs headline"><span class="l1">Your Health</span><span class="l2">is our Priority</span></h1>

  <p class="abs contact">
    42 Harbour Lane, Port Elwyn, St. Avel<br>
    Tel : (555) 310 2040 / 2041<br>
    General Practitioner - (555) 310 4471,<br>
    Ophthalmologist - (555) 310 5582,<br>
    Obstetrician/Gynaecologist –<br>
    (555) 310 6613, (555) 310 7724<br>
    Opening hours :<br>
    Monday – Fridays 9am-6pm,<br>
    Saturdays 10am – 5pm
  </p>

  <div class="abs service-icon" aria-hidden="true"></div>

  <p class="abs eye-doc">
    ClearSight Vision Services<br>
    <span class="red name">Dr. Elena R. Castillo</span><br>
    MD. Surgeon Ophthalmologist<br>
    Email: elena.castillo@example.com
  </p>

  <div class="abs vision-brand"><span class="dot"></span><span>ClearSight<br>Vision Services</span></div>

  <p class="abs gp">
    <span class="red name">Dr. Marcus Whitfield, MD.</span><br>
    Eyes disease examination,<br>
    Surgery of Pterygium, Cataract,<br>
    Glaucoma, Emergency: Conjunctivitis,<br>
    Traumatism,<br>
    Foreign body and more<br>
    General Practitioner<br>
    marcus.whitfield@example.com
  </p>

  <ul class="abs gp-list">
    <li>General Checks</li>
    <li>Annual Check ups</li>
    <li>Wound Care/Dressings</li>
    <li>Incision &amp; Drainage</li>
    <li>Suturing lacerations</li>
    <li>Pain Injections</li>
    <li>Glucose checks</li>
    <li>Foreign Body Removal</li>
  </ul>

  <div class="abs obgyn-brand"><span class="dot"></span><span>Mehra<br>Women's Care</span></div>

  <p class="abs obgyn">
    <span class="red name">Dr. Anil Mehra</span>,<br>
    BMedSci, MBBS, DM (O&amp;G), FACOG<br>
    Obstetrician &amp; Gynaecologist<br>
    <span class="red">Email:</span> dr.mehra@example.com<br>
    <span class="red">Obstetrics:</span> Prenatal Care, Delivery, Postnatal checks, High Risk pregnancy<br>
    <span class="red">Gynaecology :</span> Pap smears, Abnormal vaginal bleeding, Fibroids, Colposcopy,<br>
    Family planning, Infertility, Cancer screening, And More....
  </p>
</main>
</body>
</html>
```